Occupational Therapist does home accessibility for disabled folks; needs business card design

We need a business card for a company in Portland, Oregon that specializes in making homes accessible, comfortable, and functional for people who are disabled or aging who would like to stay in THEIR home. Our medical background as Occupational Therapists allows us to translate the functional needs of the person into the recommendations for the design of the home remodel.

Target Market(s)

Elderly, children of elderly
People with disabilities, families of people with disabilities

Industry/Entity Type

Business

Contact Information for Business Card

Company name: HomeWise
Name: Danielle Reyes Crawford, OTR/L, CAPS, ECHM
Occupational Therapist, Home Modification & Accessibility Specialist
website: www.homewiseforyears.com
email: homewiseforyears@nestmail.example
phone: (503)218-4057
CCB #: 487315

Font styles to use
Sans Serif

Requirements
Must have
• My logo
• Easy to read font with contrasting background
• Please list the Services offered: Occupational Therapy, Home safety & accessibility assessments, Home modification consulting, project management
Nice to have
• Friendly, welcoming feel
Should not have
• Dark colored background

```html
<!DOCTYPE html>
<html lang="en">
<head>
<meta charset="utf-8">
<title>HomeWise Business Card</title>
<link rel="stylesheet" href="https://fonts.googleapis.com/css2?family=Roboto:wght@400;500;700&display=swap">
<style>
  :root {
    --backdrop: #262626;
    --card-white: #ffffff;
    --brand-orange: #d08019;
    --brand-grey: #666666;
    --text-grey: #555555;
    --text-white: #ffffff;
  }
  * { box-sizing: border-box; margin: 0; padding: 0; }
  html, body {
    width: 1105px;
    height: 1200px;
    overflow: hidden;
  }
  body {
    background: var(--backdrop);
    font-family: "Roboto", Arial, sans-serif;
    position: relative;
  }
  .card {
    position: absolute;
    left: 193px;
    width: 720px;
    height: 412px;
    background: var(--card-white);
    box-shadow: 0 4px 14px rgba(0,0,0,0.55);
    overflow: hidden;
  }
  .card--front { top: 146px; }
  .card--back { top: 602px; }

  .brand-mark {
    display: flex;
    align-items: center;
    gap: 12px;
    color: var(--brand-grey);
    font-weight: 500;
    font-size: 50px;
    letter-spacing: -0.5px;
    white-space: nowrap;
  }
  .brand-mark__square {
    width: 22px;
    height: 22px;
    background: var(--brand-orange);
    flex: none;
  }

  .front-logo-zone {
    position: absolute;
    left: 0;
    top: 0;
    width: 354px;
    height: 412px;
    display: flex;
    align-items: center;
    justify-content: center;
    padding-bottom: 30px;
  }
  .front-panel {
    position: absolute;
    left: 354px;
    top: 0;
    width: 366px;
    height: 412px;
    background: var(--brand-orange);
  }
  .front-panel__corner {
    position: absolute;
    left: 0;
    top: 0;
  }
  .contact {
    position: absolute;
    right: 32px;
    top: 95px;
    text-align: right;
    color: var(--text-white);
  }
  .contact__name {
    font-size: 22px;
    font-weight: 700;
    letter-spacing: 0.6px;
    line-height: 26px;
  }
  .contact__credentials {
    font-size: 16px;
    font-weight: 700;
    line-height: 22px;
  }
  .contact__title {
    margin-top: 12px;
    font-size: 17px;
    line-height: 25px;
    text-transform: uppercase;
  }
  .contact__license {
    margin-top: 18px;
    font-size: 17px;
    line-height: 22px;
  }
  .contact__list {
    list-style: none;
    margin-top: 10px;
  }
  .contact__item {
    display: flex;
    justify-content: flex-end;
    align-items: center;
    gap: 8px;
    font-size: 17px;
    line-height: 28px;
  }
  .contact__icon { width: 17px; height: 17px; flex: none; }

  .back-logo {
    position: absolute;
    left: 0;
    right: 0;
    top: 150px;
    display: flex;
    justify-content: center;
  }
  .services {
    position: absolute;
    left: 0;
    right: 0;
    top: 290px;
    text-align: center;
  }
  .services__heading {
    color: var(--brand-orange);
    font-size: 24px;
    font-weight: 500;
    line-height: 30px;
  }
  .services__line {
    margin-top: 4px;
    color: var(--text-grey);
    font-size: 19px;
    line-height: 24px;
  }
  .services__bullet {
    display: inline-block;
    width: 7px;
    height: 7px;
    background: var(--brand-orange);
    margin: 0 8px;
    vertical-align: middle;
    position: relative;
    top: -2px;
  }
</style>
</head>
<body>
  <section class="card card--front" aria-label="Business card front">
    <div class="front-logo-zone">
      <div class="brand-mark"><span class="brand-mark__square"></span>HomeWise</div>
    </div>
    <div class="front-panel">
      <svg class="front-panel__corner" width="366" height="102" viewBox="0 0 366 102" aria-hidden="true">
        <polygon points="0,0 366,0 0,102" fill="var(--brand-grey)"/>
      </svg>
      <div class="contact">
        <p class="contact__name">DANIELLE REYES CRAWFORD</p>
        <p class="contact__credentials">OTR/L, CAPS, ECHM</p>
        <p class="contact__title">Occupational Therapist<br>Home Modification &amp;<br>Accessibility Specialist</p>
        <p class="contact__license">CCB #: 487315</p>
        <ul class="contact__list">
          <li class="contact__item">(503)218-4057
            <svg class="contact__icon" viewBox="0 0 24 24" aria-hidden="true"><path fill="#fff" d="M6.6 10.8a15.1 15.1 0 0 0 6.6 6.6l2.2-2.2c.3-.3.7-.4 1-.2 1.1.4 2.3.6 3.6.6.6 0 1 .4 1 1V20c0 .6-.4 1-1 1A17 17 0 0 1 3 4c0-.6.4-1 1-1h3.5c.6 0 1 .4 1 1 0 1.3.2 2.5.6 3.6.1.3 0 .7-.2 1z"/></svg>
          </li>
          <li class="contact__item">homewiseforyears@nestmail.example
            <svg class="contact__icon" viewBox="0 0 24 24" aria-hidden="true"><path fill="#fff" d="M2 5h20v14H2z"/><path d="M2 5l10 8 10-8" fill="none" stroke="var(--brand-orange)" stroke-width="2"/></svg>
          </li>
          <li class="contact__item">www.homewiseforyears.com
            <svg class="contact__icon" viewBox="0 0 24 24" aria-hidden="true"><circle cx="12" cy="12" r="11" fill="#fff"/><path d="M1 12h22M12 1c3 3.5 3 18.5 0 22M12 1c-3 3.5-3 18.5 0 22" fill="none" stroke="var(--brand-orange)" stroke-width="1.6"/></svg>
          </li>
        </ul>
      </div>
    </div>
  </section>

  <section class="card card--back" aria-label="Business card back">
    <div class="back-logo">
      <div class="brand-mark"><span class="brand-mark__square"></span>HomeWise</div>
    </div>
    <div class="services">
      <h2 class="services__heading">Services</h2>
      <p class="services__line">Occupational Therapy<span class="services__bullet"></span>Home safety &amp; accessibility assessments</p>
      <p class="services__line">Home modification consulting<span class="services__bullet"></span>Project management</p>
    </div>
  </section>
</body>
</html>
```